Velmora Company needs a Business Card Design

We just opened our business recently and we need a business card design. Our basic product are clothes and accessories. We would like to see designs that use bright colors like pink, light blue and purple. In addition to that kindly include also our address in the business card which our main office is located in Los Angeles, California.
The final design should communicate that we have affordable price yet high quality brand.

Target Market(s)

young and middle age women

Industry/Entity Type

Business

Contact Information for Business Card

Velmora Apparel and Accessories 3847 North Hollis St. Los Angeles California
Tel: 424-583-6094

Logo Text

Velmora's Apparel and Accessories

Font styles to use
Serif

Requirements
Must have
• there should be a graphic of a sexy lady wearing an elegant dress at the upper left corner of the business card.

```html
<!DOCTYPE html>
<html lang="en">
<head>
<meta charset="utf-8">
<title>Velmora Apparel and Accessories – Business Card</title>
<link href="https://fonts.googleapis.com/css2?family=ABeeZee&family=Arimo:wght@400;700&display=swap" rel="stylesheet">
<style>
  :root {
    --magenta-deep: #4e0832;
    --magenta: #9a0a5c;
    --magenta-bright: #cf127a;
    --pink-glow: #f4b6c6;
    --lilac: #a77bbd;
    --white: #ffffff;
  }
  html, body {
    margin: 0;
    padding: 0;
    width: 1200px;
    height: 722px;
    overflow: hidden;
    background: #ffffff;
  }
  .card {
    position: relative;
    width: 1200px;
    height: 722px;
    overflow: hidden;
  }
  .card__backdrop {
    position: absolute;
    inset: 0;
    background:
      radial-gradient(ellipse 38% 45% at 92% 86%, rgba(246, 190, 205, 0.95) 0%, rgba(236, 130, 170, 0.55) 45%, rgba(214, 40, 130, 0) 100%),
      radial-gradient(ellipse 30% 30% at 8% 100%, rgba(167, 123, 189, 0.55) 0%, rgba(167, 123, 189, 0) 100%),
      radial-gradient(ellipse 60% 65% at 48% 50%, var(--magenta-bright) 0%, var(--magenta) 55%, var(--magenta-deep) 100%);
  }
  .model-photo {
    position: absolute;
    left: 72px;
    top: 40px;
    width: 90px;
    height: 323px;
    border-radius: 40px 40px 12px 12px;
    background: linear-gradient(180deg, #5a3428 0%, #223062 28%, #2c3f7c 55%, #dcb6a0 72%, #2a2226 100%);
  }
  .contact {
    position: absolute;
    right: 635px;
    top: 285px;
    text-align: right;
    font-family: "ABeeZee", sans-serif;
    color: var(--white);
    font-size: 29px;
    line-height: 42px;
    letter-spacing: 0.5px;
    white-space: nowrap;
  }
  .contact__phone {
    margin-top: 42px;
  }
  .divider {
    position: absolute;
    left: 604px;
    top: 195px;
    width: 2px;
    height: 315px;
    background: var(--white);
  }
  .brand {
    font-family: "Arimo", sans-serif;
    color: var(--white);
    text-shadow: 2px 3px 4px rgba(60, 0, 30, 0.45);
    white-space: nowrap;
  }
  .brand__line {
    position: absolute;
    left: 636px;
    margin: 0;
    font-size: 75px;
    line-height: 77px;
  }
  .brand__line--name {
    top: 213px;
    font-size: 64px;
    line-height: 64px;
    letter-spacing: -2px;
    font-weight: 400;
  }
  .brand__line--apparel { top: 276px; font-weight: 700; }
  .brand__line--and { top: 353px; font-weight: 400; }
  .brand__line--accessories { top: 430px; font-weight: 700; }
</style>
</head>
<body>
  <div class="card">
    <div class="card__backdrop" role="img" aria-label="Abstract magenta, pink and lilac patterned background"></div>

    <div class="model-photo" role="img" aria-label="Photo of a model in an elegant dark starry mini dress and black boots"></div>

    <div class="contact">
      <div class="contact__street">3847 North Hollis St.</div>
      <div class="contact__city">Los Angeles California</div>
      <div class="contact__phone">Tel: 424-583-6094</div>
    </div>

    <div class="divider"></div>

    <div class="brand">
      <p class="brand__line brand__line--name">Velmora</p>
      <p class="brand__line brand__line--apparel">Apparel</p>
      <p class="brand__line brand__line--and">and</p>
      <p class="brand__line brand__line--accessories">Accessories</p>
    </div>
  </div>
</body>
</html>
```